Starvu Review Divorce Law Firm Folder Insert

We are a divorce law firm.

We need a flyer just like the one that is posted. For example, that allows for our Starvu reviews to be a good deed. We do like the coloring we will provide the image that goes on the bottom right. We are open to any design. Any thoughts people have, and unique designs are welcome were very happy with this example. However, we want people to know to have some background as to what would be the best option.

Again anything but again we do want the Starvu has to be the five stars in my logo has to be on there and the portion that says these different comments included

Target Market(s)

Divorce and Custody Clients

Industry/Entity Type

Legal

Requirements
Must have
• what must remain is the Starvu logo that large, and the five stars in the front in the back. What must be included is the Starvu reviews listed below. Not all of them must be used but no less than five must be used. At least one of the five

1.) “Worth the money!”
2.) “Simply the best”
3.) “So much knowledge and experience”
4.) “When life gets challenging, you want Marcus on your team!”
5.) “He made a painful divorce and custody, much easier to deal with”
6.) “Willingness to go the extra mile”
7.) “Respectful and caring”
8.) “I wouldn’t go with anyone else!”
Nice to have
• We are a divorce law firm in Harrisburg Pennsylvania. we need a Starvu review insert for our potential new clients folder. We need a hard insert flyer around 6 x 9 in height as similar possible to the one included as an attached, however we are open to any design. Since like the example so much the is a great guidepost.

We appreciate unique designs but have found one we have. To be very much to our liking. We are open to any other signs, but again. One example. Any thoughts people have, and unique designs are welcome were very happy with this example. However, we want people to know to have some background as to what would be the best option.

Attached you will find our logo, our shield by itself, the example card, and three images from which you should pick one.

one possibly to the photos can be included, but not aall three, included are three photos, only one should be used. Please pick one and use it
Should not have
• Look far off of a look that I too crazy

```html
<!DOCTYPE html>
<html lang="en">
<head>
<meta charset="utf-8">
<title>Starvu Review Insert – Law Office of Marcus R Holloway</title>
<link rel="stylesheet" href="https://fonts.googleapis.com/css2?family=Cinzel:wght@400&family=Libre+Caslon+Text:wght@400&family=Playfair+Display:wght@900&display=swap">
<style>
  :root {
    --paper: #ffffff;
    --navy: #161a40;
    --royal: #2a378e;
    --rose: #e04a5f;
    --amber: #f5a51e;
    --teal: #1fa6a3;
    --mist: #d0d1d3;
    --dot: #b9b9bb;
    --gold: #f2c12e;
    --white: #ffffff;
  }
  html, body {
    margin: 0;
    padding: 0;
    overflow: hidden;
    background: var(--paper);
  }
  .insert {
    width: 800px;
    height: 1200px;
    position: relative;
    overflow: hidden;
    background: var(--paper);
  }
  .insert svg { display: block; }
  .firm-mark { fill: var(--navy); }
  .firm-name {
    font-family: "Cinzel", Georgia, serif;
    font-weight: 400;
    fill: var(--navy);
  }
  .band { fill: var(--amber); }
  .contour { fill: none; stroke: var(--teal); stroke-width: 1.6; }
  .review-panel { fill: var(--rose); }
  .peak { fill: var(--teal); }
  .quote-line {
    font-family: "Libre Caslon Text", Georgia, serif;
    font-weight: 400;
    font-size: 80px;
    fill: var(--white);
  }
  .quote-name {
    font-family: "Playfair Display", Georgia, serif;
    font-weight: 900;
    font-size: 122px;
    fill: var(--royal);
  }
  .quote-mark {
    font-family: "Playfair Display", Georgia, serif;
    font-weight: 900;
    font-size: 300px;
    fill: var(--mist);
  }
  .review-rule { stroke: var(--white); stroke-width: 1.5; opacity: 0.6; }
  .short-review {
    font-family: "Libre Caslon Text", Georgia, serif;
    font-weight: 400;
    font-size: 17px;
    fill: var(--white);
  }
  .dot { fill: var(--dot); }
  .platform-name {
    font-family: "Libre Caslon Text", Georgia, serif;
    font-weight: 400;
    fill: var(--royal);
  }
  .star { fill: var(--gold); }
</style>
</head>
<body>
<main class="insert">
  <svg width="800" height="1200" viewBox="0 0 800 1200" xmlns="http://www.w3.org/2000/svg">
    <!-- background shapes -->
    <polygon class="band" points="0,157 800,707 800,1015 0,460"/>
    <g class="contours">
      <ellipse class="contour" cx="505" cy="620" rx="462" ry="440" transform="rotate(-18 505 620)"/>
      <ellipse class="contour" cx="505" cy="620" rx="420" ry="405" transform="rotate(-14 505 620)"/>
      <ellipse class="contour" cx="505" cy="620" rx="380" ry="370" transform="rotate(-10 505 620)"/>
      <ellipse class="contour" cx="505" cy="620" rx="340" ry="335" transform="rotate(-6 505 620)"/>
      <ellipse class="contour" cx="505" cy="620" rx="300" ry="300"/>
    </g>

    <!-- firm identity -->
    <g class="firm">
      <rect class="firm-mark" x="143" y="89" width="86" height="86"/>
      <text class="firm-name" x="247" y="111" font-size="19" textLength="196" lengthAdjust="spacingAndGlyphs">THE LAW OFFICE OF</text>
      <text class="firm-name" x="247" y="147" font-size="40" textLength="418" lengthAdjust="spacingAndGlyphs">MARCUS R HOLLOWAY</text>
    </g>

    <!-- review panel -->
    <rect class="review-panel" x="82" y="255" width="643" height="720"/>
    <g class="peaks">
      <polygon class="peak" points="721,159 788,256 654,256"/>
      <polygon class="peak" points="721,256 788,352 654,352"/>
      <polygon class="peak" points="721,352 788,447 654,447"/>
    </g>

    <g class="review-quote">
      <text class="quote-mark" x="112" y="490">&#8220;</text>
      <text class="quote-line" x="262" y="378">When</text>
      <text class="quote-line" x="178" y="440">life gets</text>
      <text class="quote-line" x="118" y="502">challenging,</text>
      <text class="quote-line" x="236" y="564">you want</text>
      <text class="quote-name" x="150" y="664">Marcus</text>
      <text class="quote-line" x="146" y="726">on your</text>
      <text class="quote-line" x="296" y="788">team!</text>
      <text class="quote-mark" x="505" y="930">&#8221;</text>
    </g>

    <g class="short-reviews">
      <line class="review-rule" x1="170" y1="848" x2="695" y2="848"/>
      <text class="short-review" x="170" y="888">&#8220;Worth the money!&#8221;</text>
      <text class="short-review" x="170" y="932">&#8220;Simply the best&#8221;</text>
      <text class="short-review" x="420" y="888">&#8220;Respectful and caring&#8221;</text>
      <text class="short-review" x="420" y="932">&#8220;I wouldn&#8217;t go with anyone else!&#8221;</text>
    </g>

    <!-- dot grid -->
    <g class="dots">
      <circle class="dot" cx="23" cy="881" r="11"/><circle class="dot" cx="82" cy="881" r="11"/><circle class="dot" cx="142" cy="881" r="11"/>
      <circle class="dot" cx="23" cy="954" r="11"/><circle class="dot" cx="82" cy="954" r="11"/><circle class="dot" cx="142" cy="954" r="11"/>
      <circle class="dot" cx="23" cy="1026" r="11"/><circle class="dot" cx="82" cy="1026" r="11"/><circle class="dot" cx="142" cy="1026" r="11"/>
      <circle class="dot" cx="23" cy="1098" r="11"/><circle class="dot" cx="82" cy="1098" r="11"/><circle class="dot" cx="142" cy="1098" r="11"/>
    </g>

    <!-- review platform and rating -->
    <text class="platform-name" x="258" y="1046" font-size="84" textLength="284" lengthAdjust="spacingAndGlyphs">Starvu</text>
    <g class="rating" aria-label="Five star rating">
      <polygon class="star" transform="translate(284 1102)" points="0,-27 6.3,-8.7 25.7,-8.3 10.2,3.3 15.9,21.8 0,10.8 -15.9,21.8 -10.2,3.3 -25.7,-8.3 -6.3,-8.7"/>
      <polygon class="star" transform="translate(341 1102)" points="0,-27 6.3,-8.7 25.7,-8.3 10.2,3.3 15.9,21.8 0,10.8 -15.9,21.8 -10.2,3.3 -25.7,-8.3 -6.3,-8.7"/>
      <polygon class="star" transform="translate(399 1102)" points="0,-27 6.3,-8.7 25.7,-8.3 10.2,3.3 15.9,21.8 0,10.8 -15.9,21.8 -10.2,3.3 -25.7,-8.3 -6.3,-8.7"/>
      <polygon class="star" transform="translate(457 1102)" points="0,-27 6.3,-8.7 25.7,-8.3 10.2,3.3 15.9,21.8 0,10.8 -15.9,21.8 -10.2,3.3 -25.7,-8.3 -6.3,-8.7"/>
      <polygon class="star" transform="translate(514 1102)" points="0,-27 6.3,-8.7 25.7,-8.3 10.2,3.3 15.9,21.8 0,10.8 -15.9,21.8 -10.2,3.3 -25.7,-8.3 -6.3,-8.7"/>
    </g>
  </svg>
</main>
</body>
</html>
```